Vodka Bottle Label - Lune Vodka

I need a bottle label for a vodka I'd like to make called Lune Vodka.
I would like a label that looks elegant and fresh. I would like some mountains and colours to be red and white. Open to other colours being added but not too colourful. "Lune" means fresh, dawn in polish, i would like if mountains or something extra was added to the label too. I would like the Lune Vodka name not to be too small.
The vodka is made in australia and is 37%.

I would love to have a little bit of gold colour in the label!

I will provide the back label words when completing my decision.

i'd like to make it more simple and less european looking. More australian.

I saw a bottle like this and i did like the concept.

https://www.oakbarrelcellars.com.au/spirits/grey-vodka-range?srsltid=XqTz81mwkPLd04-hr-q7w93nfbzkgd_mR2yTpaMWxJeQ6vcbTnZsLpo

Target Market(s)

Vodka Drinkers

Industry/Entity Type

Alcohol

Colors
EB3D1F
EC4F4E
F09395
F8D3D4
FCEDEE

Requirements
Must have
• red and white colours incorporated, mountains or freshness on it.
Nice to have
• Fresh and clean look. Classy

```html
<!DOCTYPE html>
<html lang="en">
<head>
<meta charset="utf-8">
<title>Lune Vodka – Bottle Label</title>
<link rel="stylesheet" href="https://fonts.googleapis.com/css2?family=Marcellus&family=Josefin+Sans:wght@300;400;600&display=swap">
<style>
  :root {
    --stage-top: #d3dbe8;
    --stage-mid: #e4e8ef;
    --stage-low: #b9c6da;
    --paper: #ffffff;
    --label-frame: #d6d9f4;
    --coral: #eb4f3a;
    --rose: #ec4f4e;
    --blush: #f8d3d4;
    --snow: #fcedee;
    --white: #ffffff;
    --serif: "Marcellus", Georgia, serif;
    --sans: "Josefin Sans", "Helvetica Neue", Arial, sans-serif;
  }
  * { margin: 0; padding: 0; box-sizing: border-box; }
  html, body { width: 1200px; height: 2475px; overflow: hidden; background: var(--paper); }
  .canvas { position: relative; width: 1200px; height: 2475px; }
  .stage {
    position: absolute; left: 0; top: 0; width: 1200px; height: 1968px;
    background: linear-gradient(180deg, var(--stage-top) 0%, var(--stage-mid) 45%, var(--stage-mid) 75%, var(--stage-low) 100%);
  }
  .front-label { position: absolute; left: 402px; top: 828px; width: 426px; height: 844px; }
  .front-label svg { display: block; width: 100%; height: 100%; }
  .label-eyebrow { font-family: var(--sans); font-weight: 400; font-size: 23px; letter-spacing: 9px; fill: var(--coral); }
  .label-brand { font-family: var(--serif); font-size: 178px; letter-spacing: 22px; fill: var(--white); }
  .label-kind { font-family: var(--sans); font-weight: 300; font-size: 58px; letter-spacing: 14px; fill: var(--white); }
  .label-origin { font-family: var(--sans); font-weight: 400; font-size: 40px; letter-spacing: 10px; fill: var(--blush); }
  .label-note { font-family: var(--sans); font-weight: 400; font-size: 21px; letter-spacing: 7px; fill: var(--snow); }
  .label-strength { font-family: var(--sans); font-weight: 600; font-size: 29px; letter-spacing: 2px; fill: var(--snow); }
  .wordmark { position: absolute; left: 0; width: 1200px; text-align: center; color: var(--rose); font-family: var(--serif); font-weight: 400; white-space: nowrap; }
  .wordmark-name { top: 2154px; font-size: 120px; line-height: 120px; letter-spacing: 14px; padding-left: 14px; }
  .wordmark-kind { top: 2266px; font-size: 42px; line-height: 42px; letter-spacing: 14px; padding-left: 14px; }
</style>
</head>
<body>
<main class="canvas">
  <section class="stage">
    <div class="front-label">
      <svg viewBox="0 0 640 1264" xmlns="http://www.w3.org/2000/svg">
        <defs>
          <linearGradient id="labelFill" x1="0" y1="0" x2="1" y2="0">
            <stop offset="0" stop-color="#30358f"/>
            <stop offset="0.5" stop-color="#4349a6"/>
            <stop offset="1" stop-color="#2d3289"/>
          </linearGradient>
          <linearGradient id="sceneFill" x1="0" y1="0" x2="0" y2="1">
            <stop offset="0" stop-color="#4a8fd8" stop-opacity="0"/>
            <stop offset="0.2" stop-color="#4a93d8" stop-opacity="0.85"/>
            <stop offset="0.45" stop-color="#3467b8"/>
            <stop offset="0.66" stop-color="#141c45"/>
            <stop offset="0.84" stop-color="#2b3275"/>
            <stop offset="1" stop-color="#4047a0" stop-opacity="0"/>
          </linearGradient>
          <clipPath id="labelShape">
            <polygon points="320,0 640,105 640,1150 320,1264 0,1150 0,105"/>
          </clipPath>
        </defs>

        <polygon class="label-body" points="320,0 640,105 640,1150 320,1264 0,1150 0,105" fill="url(#labelFill)"/>

        <g class="label-illustration" clip-path="url(#labelShape)">
          <rect x="0" y="300" width="640" height="534" fill="url(#sceneFill)" role="img" aria-label="Watercolour mountain range with snowy peaks above a pine forest reflected in a still lake"/>
        </g>

        <polyline class="label-frame" fill="none" stroke="var(--label-frame)" stroke-width="2"
          points="320,16 600,108 600,130 624,130 624,1126 600,1126 600,1146 320,1246 40,1146 40,1126 16,1126 16,130 40,130 40,108 320,16"/>

        <circle class="label-mark" cx="320" cy="135" r="12" fill="none" stroke="var(--coral)" stroke-width="3"/>
        <text class="label-eyebrow" x="324" y="221" text-anchor="middle">HANDCRAFTED</text>

        <text class="label-brand" x="331" y="646" text-anchor="middle">LUNE</text>
        <text class="label-kind" x="327" y="726" text-anchor="middle">VODKA</text>

        <g class="label-origin-band" clip-path="url(#labelShape)">
          <polygon points="0,950 640,776 640,884 0,1058" fill="var(--coral)"/>
          <text class="label-origin" x="326" y="935" text-anchor="middle" transform="rotate(-15 326 921)">AUSTRALIA</text>
        </g>

        <text class="label-note" x="323" y="1094" text-anchor="middle">GLUTEN-FREE</text>
        <text class="label-strength" x="320" y="1150" text-anchor="middle">37% ALC/ 70 CL</text>
      </svg>
    </div>
  </section>

  <div class="wordmark wordmark-name">LUNE</div>
  <div class="wordmark wordmark-kind">VODKA</div>
</main>
</body>
</html>
```